Vial Crate Guild - A Monthly Subscription for Essential Oils - Shopify Website Design

A monthly subscription company. Need a Shopify Website Design and uploaded to fully work with Tidy Renewals.

Please look at these sites for examples as well as the images I enclosed.

https://purelymeadow.example/
https://www.bloomup-ax.example/
https://www.dinnerkitly.example/
https://www.globalsnackos.example/

Number of Pages Required

1 page

```html
<!DOCTYPE html>
<html lang="en">
<head>
<meta charset="utf-8">
<title>Vial Crate Guild – Essential Oil Subscription</title>
<link href="https://fonts.googleapis.com/css2?family=Montserrat:wght@600;700;800&family=Poppins:wght@400;500;600;700&display=swap" rel="stylesheet">
<style>
:root{
  --brown:#6e4a3c;
  --brown-dark:#6a4839;
  --olive:#8a9a32;
  --olive-light:#a8b65a;
  --text:#5e4a40;
  --muted:#7a6a62;
  --pale:#f4f9fa;
  --white:#ffffff;
  --line:#b9a59c;
}
*{box-sizing:border-box;margin:0;padding:0}
html,body{width:1200px;height:3736px;overflow:hidden}
body{position:relative;background:var(--white);font-family:"Poppins",sans-serif;color:var(--text)}
.abs{position:absolute}
.heading{font-family:"Montserrat",sans-serif;font-weight:700;color:var(--brown)}
.btn{position:absolute;display:flex;align-items:center;justify-content:center;border-radius:16px;background:var(--olive);color:#fff;font:600 10px "Poppins",sans-serif;letter-spacing:.5px;text-transform:uppercase}
.btn-outline{background:transparent;border:2px solid var(--olive);color:var(--olive)}
.photo{position:absolute}

/* header */
.site-header{position:absolute;left:0;top:0;width:1200px;height:75px;background:#fff}
.brand{position:absolute;left:157px;top:22px;display:flex;align-items:center;gap:10px}
.brand-dot{width:22px;height:22px;border-radius:50%;background:var(--brown)}
.brand-name{font:600 12px/1.1 "Poppins",sans-serif;color:var(--brown);width:80px}
.nav a{position:absolute;top:33px;font:600 11px "Poppins",sans-serif;color:var(--brown);text-decoration:none}
.search{position:absolute;left:852px;top:26px;width:149px;height:29px;border:2px solid var(--olive);border-radius:15px;font:400 10px "Poppins",sans-serif;color:var(--muted);padding:7px 14px}
.search svg{position:absolute;right:12px;top:6px}
.cart{position:absolute;left:1024px;top:30px}

/* hero */
.hero{position:absolute;left:0;top:75px;width:1200px;height:600px;background:linear-gradient(90deg,#eef1f2 0%,#e4e7e6 35%,#b87a3a 55%,#8a4e1e 68%,#dfe6e2 85%,#cfe0d0 100%)}
.hero-title{position:absolute;left:155px;top:312px;font:800 41px "Montserrat",sans-serif;color:var(--brown);letter-spacing:.5px}
.hero-sub{position:absolute;left:158px;top:363px;font:400 16px "Poppins",sans-serif;color:var(--brown)}
.hero-sub span{color:var(--olive)}

/* features */
.feature{position:absolute;top:708px;display:flex;gap:14px}
.feature h3{font:700 14px "Poppins",sans-serif;color:var(--brown);margin-bottom:2px}
.feature p{font:400 11px/1.15 "Poppins",sans-serif;color:var(--text);width:190px}

/* plans */
.plans{position:absolute;left:0;top:794px;width:1200px;height:602px;background:var(--pale)}
.leaf{position:absolute;background:radial-gradient(ellipse at center,rgba(120,180,170,.35),rgba(120,180,170,0) 70%)}
.card{position:absolute;background:#fff;box-shadow:0 2px 10px rgba(0,0,0,.08);text-align:center}
.card h3{font:700 15px "Poppins",sans-serif;color:var(--brown);margin-top:20px}
.card p{font:400 12px/1.25 "Poppins",sans-serif;color:var(--brown);margin:6px auto 0;width:230px}

/* split sections */
.bullets{list-style:none}
.bullets li{position:relative;padding-left:23px;font:400 12.5px "Poppins",sans-serif;color:#8c6b5e;height:34.8px}
.bullets li::before{content:"";position:absolute;left:0;top:6px;width:7px;height:7px;border-radius:50%;background:var(--brown)}
.section-title{font:700 22px "Poppins",sans-serif;color:var(--brown)}

/* testimonials */
.testimonials{position:absolute;left:0;top:2296px;width:1200px;height:618px;background:var(--pale)}
.quote{position:absolute;top:136px;width:254px;height:252px;background:#fff;box-shadow:0 2px 10px rgba(0,0,0,.07);border-radius:4px;padding:30px 16px;text-align:center;font:400 12px/22.5px "Poppins",sans-serif;color:#8c6b5e}
.quote::after{content:"";position:absolute;right:56px;bottom:-26px;border-left:18px solid transparent;border-right:18px solid transparent;border-top:26px solid #fff}
.avatar{position:absolute;top:443px;width:73px;height:73px;border-radius:50%;background:radial-gradient(circle,#f3b652,#e99a2e)}
.person{position:absolute;top:528px;width:160px;text-align:center;font:600 12.5px "Poppins",sans-serif;color:var(--brown)}

/* blogs */
.post{position:absolute;border:1px solid #b8a098;background:#fff}
.post h4{font:700 15px "Poppins",sans-serif;color:var(--brown)}
.post time{display:block;font:400 10px "Poppins",sans-serif;color:var(--olive);margin-top:1px}
.post p{font:400 12px/22px "Poppins",sans-serif;color:#8c6b5e;margin-top:6px}
.post p b{color:var(--olive);font-weight:700}
.thumb{position:absolute;background:linear-gradient(135deg,#6e8a3a 0%,#3f4a26 45%,#6a3a1c 70%,#c66a2a 100%)}

/* footer */
.site-footer{position:absolute;left:0;top:3559px;width:1200px;height:177px;background:var(--brown-dark);color:#fff}
.foot-col{position:absolute;top:36px}
.foot-col h5{font:700 11px "Poppins",sans-serif;letter-spacing:.5px;margin-bottom:2px}
.foot-col a{display:block;font:400 12px/22.5px "Poppins",sans-serif;color:#fff;text-decoration:none}
.newsletter{position:absolute;left:818px;top:83px;width:224px;height:29px;background:#fff;border-radius:15px}
.newsletter span{position:absolute;left:14px;top:8px;font:400 10px "Poppins",sans-serif;color:var(--brown)}
.newsletter b{position:absolute;right:0;top:0;width:74px;height:29px;border-radius:15px;background:var(--olive);font:600 10px/29px "Poppins",sans-serif;text-align:center;color:#fff}
</style>
</head>
<body>

<header class="site-header">
  <div class="brand"><span class="brand-dot"></span><span class="brand-name">Vial Crate Guild</span></div>
  <nav class="nav">
    <a style="left:576px">Shop</a>
    <a style="left:646px">FAQs</a>
    <a style="left:717px">Blog</a>
    <a style="left:784px">Contact</a>
  </nav>
  <div class="search">Search
    <svg width="14" height="14" viewBox="0 0 14 14"><circle cx="6" cy="6" r="4.5" fill="none" stroke="#6e4a3c" stroke-width="1.8"/><line x1="9.3" y1="9.3" x2="13" y2="13" stroke="#6e4a3c" stroke-width="1.8"/></svg>
  </div>
  <svg class="cart" width="18" height="16" viewBox="0 0 18 16"><path d="M1 1h3l2 9h9l2-6H5" fill="none" stroke="#8a9a32" stroke-width="1.8"/><circle cx="7" cy="14" r="1.5" fill="#8a9a32"/><circle cx="14" cy="14" r="1.5" fill="#8a9a32"/></svg>
</header>

<section class="hero">
  <div class="photo" role="img" aria-label="Amber essential oil bottles with white stones, a towel and a glass candle holder" style="inset:0"></div>
</section>
<h1 class="hero-title">Pure Essential Oil</h1>
<p class="hero-sub">Get <span>30%</span> Dscount for the month of Novemeber</p>
<a class="btn btn-outline" style="left:160px;top:402px;width:148px;height:28px">Get Discount</a>
<a class="btn" style="left:324px;top:402px;width:149px;height:28px">Shop Now</a>

<div class="feature" style="left:157px">
  <svg width="28" height="36" viewBox="0 0 28 36"><rect x="10" y="2" width="8" height="6" fill="#8a9a32"/><path d="M6 12h16l3 6v14H3V18z" fill="#8a9a32"/><circle cx="14" cy="24" r="4" fill="#fff"/></svg>
  <div><h3>Choose from Different Kinds</h3><p>Lorem ipsum dolor sit amet, consectetur adipiscing elit</p></div>
</div>
<div class="feature" style="left:502px">
  <svg width="34" height="36" viewBox="0 0 34 36"><path d="M4 4c14 0 26 6 24 20-2 10-14 10-18 4C4 22 6 10 4 4z" fill="#8a9a32"/><path d="M8 8c6 8 10 16 12 26" stroke="#fff" stroke-width="1.5" fill="none"/></svg>
  <div><h3>Natural and Pure</h3><p>Lorem ipsum dolor sit amet, consectetur adipiscing elit</p></div>
</div>
<div class="feature" style="left:806px">
  <svg width="36" height="36" viewBox="0 0 36 36"><circle cx="18" cy="18" r="15" fill="none" stroke="#8a9a32" stroke-width="2.5"/><circle cx="18" cy="18" r="10" fill="#8a9a32"/><text x="18" y="23" text-anchor="middle" font-family="Poppins,sans-serif" font-size="13" font-weight="700" fill="#fff">$</text></svg>
  <div><h3>1-Month Money Back</h3><p>Lorem ipsum dolor sit amet, consectetur adipiscing elit</p></div>
</div>

<section class="plans">
  <div class="leaf" role="img" aria-label="Watercolour leaf sprig" style="left:-20px;top:0;width:190px;height:160px"></div>
  <div class="leaf" role="img" aria-label="Watercolour leaf sprig" style="left:980px;top:-30px;width:240px;height:140px"></div>
  <div class="leaf" role="img" aria-label="Watercolour leaf sprig" style="left:0;top:380px;width:210px;height:220px"></div>
  <div class="leaf" role="img" aria-label="Watercolour leaf sprig" style="left:1030px;top:300px;width:180px;height:260px"></div>
</section>

<article class="card" style="left:158px;top:908px;width:263px;height:383px">
  <div class="photo" role="img" aria-label="Essential oil bottle surrounded by purple flowers" style="left:0;top:0;width:263px;height:225px;background:linear-gradient(160deg,#f3f2f4 0%,#e8dde8 45%,#b88a2e 60%,#8f6bb0 85%,#f1eef1 100%)"></div>
  <div style="position:absolute;top:225px;left:0;right:0">
    <h3>Pure Essential Oil</h3>
    <p>Lorem ipsum dolor sit amet, consectetur adipiscing elitorem ipsum dolor sit amet, consectetur</p>
  </div>
  <a class="btn" style="left:62px;top:331px;width:149px;height:29px">Shop</a>
</article>

<article class="card" style="left:451px;top:871px;width:299px;height:457px">
  <div class="photo" role="img" aria-label="Amber oil bottles among yellow and pink wildflowers on wood" style="left:0;top:0;width:299px;height:299px;background:linear-gradient(170deg,#9fae3a 0%,#6d5b2a 40%,#4e2f1a 60%,#c07aa8 85%,#8a5a40 100%)"></div>
  <div style="position:absolute;top:299px;left:0;right:0">
    <h3>Monthly Subscription</h3>
    <p>Lorem ipsum dolor sit amet, consectetur adipiscing elitorem ipsum dolor sit amet, consectetur</p>
  </div>
  <a class="btn" style="left:81px;top:406px;width:149px;height:29px">See Plans</a>
</article>

<article class="card" style="left:781px;top:908px;width:261px;height:383px">
  <div class="photo" role="img" aria-label="Yellow oil bottle and dropper with chamomile flowers" style="left:0;top:0;width:261px;height:225px;background:linear-gradient(150deg,#ffffff 0%,#f4eed8 40%,#e9c23a 60%,#9bb05a 80%,#ffffff 100%)"></div>
  <div style="position:absolute;top:225px;left:0;right:0">
    <h3>Other Oil</h3>
    <p>Lorem ipsum dolor sit amet, consectetur adipiscing elitorem ipsum dolor sit amet, consectetur</p>
  </div>
  <a class="btn" style="left:62px;top:331px;width:149px;height:29px">Shop</a>
</article>

<!-- promising results -->
<div class="photo" role="img" aria-label="Glass dropper above an amber bottle with lavender and greenery behind" style="left:0;top:1396px;width:599px;height:450px;background:linear-gradient(140deg,#8a8fb0 0%,#6e8a3e 30%,#d9823a 55%,#4a3420 75%,#7c9a4a 100%)"></div>
<div class="leaf" role="img" aria-label="Line-drawn leaf sprig" style="left:600px;top:1396px;width:150px;height:80px;background:radial-gradient(ellipse,rgba(90,90,90,.18),rgba(90,90,90,0) 70%)"></div>
<div class="leaf" role="img" aria-label="Line-drawn leaf sprig" style="left:1060px;top:1600px;width:140px;height:240px;background:radial-gradient(ellipse,rgba(90,90,90,.18),rgba(90,90,90,0) 70%)"></div>
<h2 class="section-title abs" style="left:670px;top:1474px">Promising Results</h2>
<ul class="bullets abs" style="left:670px;top:1523px">
  <li>Lorem ipsum dolor sit amet, consectetur adipiscing elit</li>
  <li>Quis ipsum suspendisse ultrices gravida.</li>
  <li>Quis ipsum suspendisse ultrices gravida.</li>
  <li>Lorem ipsum dolor sit amet, consectetur adipiscing elit</li>
  <li>Quis ipsum suspendisse ultrices gravida.</li>
  <li>Quis ipsum suspendisse ultrices gravida.</li>
</ul>
<a class="btn" style="left:670px;top:1733px;width:151px;height:29px">See Plans</a>

<!-- what's in the box -->
<div class="leaf" role="img" aria-label="Line-drawn leaf sprig" style="left:400px;top:1846px;width:200px;height:110px;background:radial-gradient(ellipse,rgba(90,90,90,.18),rgba(90,90,90,0) 70%)"></div>
<div class="leaf" role="img" aria-label="Line-drawn leaf sprig" style="left:0;top:2060px;width:140px;height:230px;background:radial-gradient(ellipse,rgba(90,90,90,.18),rgba(90,90,90,0) 70%)"></div>
<h2 class="section-title abs" style="left:157px;top:1923px">What’s in the box?</h2>
<ul class="bullets abs" style="left:157px;top:1973px">
  <li>Lorem ipsum dolor sit amet, consectetur adipiscing elit</li>
  <li>Quis ipsum suspendisse ultrices gravida.</li>
  <li>Quis ipsum suspendisse ultrices gravida.</li>
  <li>Lorem ipsum dolor sit amet, consectetur adipiscing elit</li>
  <li>Quis ipsum suspendisse ultrices gravida.</li>
  <li>Quis ipsum suspendisse ultrices gravida.</li>
</ul>
<a class="btn" style="left:157px;top:2184px;width:150px;height:29px">See Plans</a>
<div class="photo" role="img" aria-label="Dropper bottle with birch leaves, scissors and a mortar on burlap and wood" style="left:599px;top:1846px;width:601px;height:450px;background:linear-gradient(160deg,#9a8468 0%,#6e5a40 35%,#4a2e18 55%,#6f8e3a 75%,#8a7358 100%)"></div>

<section class="testimonials">
  <div class="leaf" role="img" aria-label="Watercolour leaf sprig" style="left:0;top:380px;width:220px;height:220px"></div>
  <div class="leaf" role="img" aria-label="Watercolour leaf sprig" style="left:1030px;top:320px;width:180px;height:270px"></div>
  <h2 class="section-title abs" style="left:0;width:1200px;text-align:center;top:70px">What Our Customers Say</h2>

  <blockquote class="quote" style="left:158px">Lorem ipsum dolor sit amet, consectetur adipiscing elit, sed do eiusmod tempor incididunt ut labore et dolore magna aliqua. Quis ipsum suspendisse ultrices gravida. Risus commodo viverra maecenas accumsan lacus vel facilisis.</blockquote>
  <blockquote class="quote" style="left:473px">Lorem ipsum dolor sit amet, consectetur adipiscing elit, sed do eiusmod tempor incididunt ut labore et dolore magna aliqua. Quis ipsum suspendisse ultrices gravida. Risus commodo viverra maecenas accumsan lacus vel facilisis.</blockquote>
  <blockquote class="quote" style="left:788px">Lorem ipsum dolor sit amet, consectetur adipiscing elit, sed do eiusmod tempor incididunt ut labore et dolore magna aliqua. Quis ipsum suspendisse ultrices gravida. Risus commodo viverra maecenas accumsan lacus vel facilisis.</blockquote>

  <div class="avatar" role="img" aria-label="Customer portrait" style="left:316px"></div>
  <div class="avatar" role="img" aria-label="Customer portrait" style="left:631px"></div>
  <div class="avatar" role="img" aria-label="Customer portrait" style="left:946px"></div>
  <div class="person" style="left:272px">John Doe</div>
  <div class="person" style="left:588px">Han Doyun</div>
  <div class="person" style="left:903px">Seo Minjae</div>
</section>

<h2 class="section-title abs" style="left:0;width:1200px;text-align:center;top:2981px">Blogs</h2>

<article class="post" style="left:158px;top:3051px;width:434px;height:431px">
  <div class="thumb" role="img" aria-label="Glass dropper above an amber oil bottle" style="left:0;top:0;width:432px;height:298px"></div>
  <div style="position:absolute;left:22px;top:309px;right:18px">
    <h4>Essential Oli Essential Oli</h4>
    <time>October 29, 2020</time>
    <p>Lorem ipsum dolor sit amet, consectetur adipiscing elit, sed do eiusmod tempor incididunt ut labore et dolore magna aliqua. Quis ipsum suspendisse ultrices gravida <b>[...]</b></p>
  </div>
</article>

<article class="post" style="left:609px;top:3053px;width:436px;height:134px">
  <div class="thumb" role="img" aria-label="Glass dropper above an amber oil bottle" style="left:0;top:0;width:133px;height:132px"></div>
  <div style="position:absolute;left:152px;top:10px;right:10px">
    <h4>Essential Oli Essential Oli</h4><time>October 29, 2020</time>
    <p>Lorem ipsum dolor sit amet, consectetur et dolore magna aliqua. Quis ipsum suspendisse ultrices gravida <b>[...]</b></p>
  </div>
</article>
<article class="post" style="left:609px;top:3202px;width:436px;height:134px">
  <div class="thumb" role="img" aria-label="Glass dropper above an amber oil bottle" style="left:0;top:0;width:133px;height:132px"></div>
  <div style="position:absolute;left:152px;top:10px;right:10px">
    <h4>Essential Oli Essential Oli</h4><time>October 29, 2020</time>
    <p>Lorem ipsum dolor sit amet, consectetur et dolore magna aliqua. Quis ipsum suspendisse ultrices gravida <b>[...]</b></p>
  </div>
</article>
<article class="post" style="left:609px;top:3351px;width:436px;height:134px">
  <div class="thumb" role="img" aria-label="Glass dropper above an amber oil bottle" style="left:0;top:0;width:133px;height:132px"></div>
  <div style="position:absolute;left:152px;top:10px;right:10px">
    <h4>Essential Oli Essential Oli</h4><time>October 29, 2020</time>
    <p>Lorem ipsum dolor sit amet, consectetur et dolore magna aliqua. Quis ipsum suspendisse ultrices gravida <b>[...]</b></p>
  </div>
</article>

<footer class="site-footer">
  <div class="brand" style="top:44px;gap:12px"><span class="brand-dot" style="background:#fff"></span><span class="brand-name" style="color:#fff;font-size:14px;width:110px">Vial Crate Guild</span></div>
  <div class="foot-col" style="left:350px"><h5>QUICK LINKS</h5><a>FAQs</a><a>Resources</a><a>Blogs</a></div>
  <div class="foot-col" style="left:585px"><h5>INFORMATION</h5><a>About Us</a><a>Contact Us</a><a>Terms &amp; Coniditions</a><a>Private Privacy</a></div>
  <div class="foot-col" style="left:818px"><h5>JOIN OUR NEWSLETTER</h5><a>Lorem ipsum dolor sit amet</a></div>
  <div class="newsletter"><span>Your Email</span><b>SUBMIT</b></div>
</footer>

</body>
</html>
```